Painting Contractor Business Card Design

We are looking for a cool, bold, modern, polished, business card design. We are a high-end residential painting contractor. Please incorporate our logo and keep with our green/black color scheme. We are interested in seeing 2-sided and 1-sided options. Thank you very much!

Industry/Entity Type

Business

Contact Information for Business Card

Info for the card:
Owen Talsky
mobile 206-555-0193
email owen@kestrowfinish.net
web www.kestrowfinish.net

```html
<!DOCTYPE html>
<html lang="en">
<head>
<meta charset="utf-8">
<title>Kestrow Finish – Business Card</title>
<link rel="stylesheet" href="https://fonts.googleapis.com/css2?family=Jost:wght@500;600;700&display=swap">
<style>
  :root {
    --ink: #333333;
    --frame: #2e2e2e;
    --paper: #ffffff;
    --brand-green: #3aa345;
    --slate: #7f9cbd;
    --blue-light: #7fc0ea;
    --green: #85d3a8;
    --teal: #86d6cc;
    --mint: #9fd8b3;
    --coral: #f4907a;
    --peach: #f6b67f;
    --yellow: #f9d98a;
    --lime: #dbe595;
    --leaf: #b4d98a;
    --band-blue-a: #244f86;
    --band-blue-b: #2aa3e2;
    --band-green-a: #78bf43;
    --band-green-b: #2fb77c;
    --band-orange-a: #ef5a3a;
    --band-orange-b: #f6993a;
  }
  html, body {
    margin: 0;
    width: 927px;
    height: 1200px;
    overflow: hidden;
    background: var(--paper);
    font-family: "Jost", "Century Gothic", sans-serif;
  }
  .sheet { position: relative; width: 927px; height: 1200px; }
  .card {
    position: absolute;
    left: 112px;
    width: 677px;
    height: 388px;
    box-sizing: border-box;
    border: 2px solid var(--frame);
    background: var(--paper);
    overflow: hidden;
  }
  .card--front { top: 102px; }
  .card--back { top: 675px; }

  .color-field {
    position: absolute;
    left: 0;
    width: 100%;
  }
  .color-field--top {
    top: 0;
    height: 112px;
    background:
      linear-gradient(to bottom, rgba(255,255,255,0) 40%, var(--paper) 100%),
      linear-gradient(90deg, var(--slate) 0%, var(--blue-light) 30%, var(--green) 50%, var(--teal) 72%, var(--mint) 100%);
  }
  .color-field--bottom {
    bottom: 0;
    height: 108px;
    background:
      linear-gradient(to top, rgba(255,255,255,0) 40%, var(--paper) 100%),
      linear-gradient(90deg, var(--coral) 0%, var(--peach) 28%, var(--yellow) 52%, var(--lime) 76%, var(--leaf) 100%);
  }

  .wordmark {
    position: absolute;
    left: 38px;
    top: 147px;
    display: flex;
    align-items: center;
    gap: 22px;
  }
  .wordmark__square {
    width: 82px;
    height: 82px;
    background: var(--brand-green);
  }
  .wordmark__name {
    font-weight: 600;
    font-size: 54px;
    letter-spacing: 2px;
    color: var(--ink);
    white-space: nowrap;
  }

  .holder {
    position: absolute;
    left: 36px;
    top: 14px;
    margin: 0;
    font-weight: 700;
    font-size: 80px;
    line-height: 1.1;
    color: var(--ink);
    letter-spacing: 0.5px;
    white-space: nowrap;
  }
  .contact {
    position: absolute;
    left: 0;
    display: flex;
    align-items: center;
    box-sizing: border-box;
    color: #fff;
    font-weight: 500;
    font-size: 30px;
    white-space: nowrap;
  }
  .contact--phone {
    top: 137px; width: 258px; height: 55px;
    padding-left: 36px;
    background: linear-gradient(100deg, var(--band-blue-a) 0%, var(--band-blue-a) 45%, var(--band-blue-b) 100%);
  }
  .contact--email {
    top: 217px; width: 503px; height: 54px;
    justify-content: flex-end; padding-right: 17px;
    background: linear-gradient(100deg, var(--band-green-a) 0%, var(--band-green-a) 40%, var(--band-green-b) 100%);
  }
  .contact--web {
    top: 296px; width: 638px; height: 53px;
    justify-content: flex-end; padding-right: 25px;
    background: linear-gradient(100deg, var(--band-orange-a) 0%, var(--band-orange-a) 45%, var(--band-orange-b) 100%);
  }
</style>
</head>
<body>
<main class="sheet">

  <section class="card card--front" aria-label="Card front">
    <div class="color-field color-field--top" role="img" aria-label="Decorative band of translucent blue and green paint-chip shapes"></div>
    <div class="color-field color-field--bottom" role="img" aria-label="Decorative band of translucent red, orange, yellow and green paint-chip shapes"></div>
    <div class="wordmark">
      <span class="wordmark__square" aria-hidden="true"></span>
      <span class="wordmark__name">KESTROW FINISH</span>
    </div>
  </section>

  <section class="card card--back" aria-label="Card back">
    <h1 class="holder">Owen Talsky</h1>
    <div class="contact contact--phone">206·555·0193</div>
    <div class="contact contact--email">owen@kestrowfinish.net</div>
    <div class="contact contact--web">www.kestrowfinish.net</div>
  </section>

</main>
</body>
</html>
```